Borrowdale Equity Business Card

Looking for a design for our business cards. Need to look corporate and outstanding. I have enclosed our logos for the company. Borrowdale equity is an investment firm for high level clients looking for advisory in their investments. White background or black is good. We will like to double sided options maybe at the back with just the logo of the firm.

Example of the info for the business card:

Marcus Heller
Managing Director

Panama Phone +507 391 4786
Switzerland Phone +41 43 917 2648
test@borrowdale-equity-example.com
www.borrowdale-equity-example.com

Industry/Entity Type

Investment

```html
<!DOCTYPE html>
<html lang="en">
<head>
<meta charset="utf-8">
<title>Borrowdale Equity Business Card</title>
<link rel="stylesheet" href="https://fonts.googleapis.com/css2?family=Cinzel:wght@500;600&family=Dosis:wght@400;500&display=swap">
<style>
  :root {
    --page: #ecebe8;
    --card: #ffffff;
    --navy: #2b3f8f;
    --navy-light: #3a56a6;
    --navy-dark: #233679;
    --ink: #2a2a2e;
    --white: #ffffff;
    --shadow: rgba(0, 0, 0, 0.18);
  }
  * { margin: 0; padding: 0; box-sizing: border-box; }
  html, body { width: 1200px; height: 1200px; overflow: hidden; background: var(--page); }
  .canvas { position: relative; width: 1200px; height: 1200px; }

  .card {
    position: absolute; left: 126px; width: 948px; height: 556px;
    background: var(--card); box-shadow: 0 6px 18px var(--shadow); overflow: hidden;
  }
  .card--front { top: 22px; }
  .card--back { top: 622px; }

  .wordmark {
    position: absolute; left: 0; right: 0; text-align: center;
    font-family: "Cinzel", serif; font-weight: 600; color: var(--navy);
    line-height: 1;
  }
  .wordmark__line1 { display: block; font-size: 54px; letter-spacing: 2px; }
  .wordmark__line2 { display: block; font-size: 30px; letter-spacing: 12px; margin-top: 10px; }
  .card--front .wordmark { top: 104px; }
  .card--back .wordmark { top: 198px; }

  .info-band {
    position: absolute; left: 0; top: 296px; width: 948px; height: 260px;
    background: linear-gradient(180deg, var(--navy-light) 0%, var(--navy) 55%, var(--navy-dark) 100%);
  }
  .band-edge { position: absolute; left: 0; top: 0; }

  .person {
    position: absolute; left: 140px; width: 320px; top: 96px; text-align: center; color: var(--white);
  }
  .person__name { font-family: "Cinzel", serif; font-weight: 500; font-size: 33px; letter-spacing: 1px; line-height: 1; }
  .person__title { font-family: "Dosis", sans-serif; font-size: 23px; margin-top: 8px; letter-spacing: 0.5px; }

  .divider { position: absolute; left: 467px; top: 54px; width: 2px; height: 166px; background: rgba(255,255,255,0.85); }

  .contact { position: absolute; left: 516px; top: 58px; list-style: none; }
  .contact__item {
    display: flex; align-items: center; height: 40px;
    font-family: "Dosis", sans-serif; font-size: 23px; color: var(--white); letter-spacing: 0.3px;
  }
  .contact__icon { width: 22px; height: 22px; margin-right: 14px; flex: none; }

  .url-band { position: absolute; left: 0; top: 466px; width: 948px; height: 64px; }
  .url-band__text {
    position: absolute; left: 130px; right: 0; top: 0; height: 64px; line-height: 64px; text-align: center;
    font-family: "Cinzel", serif; font-weight: 600; font-size: 22px; color: var(--white); letter-spacing: 1.5px;
  }
</style>
</head>
<body>
<main class="canvas">

  <section class="card card--front" aria-label="Business card front">
    <div class="wordmark">
      <span class="wordmark__line1">Borrowdale</span>
      <span class="wordmark__line2">Equity</span>
    </div>

    <div class="info-band">
      <svg class="band-edge" width="200" height="260" viewBox="0 0 200 260" aria-hidden="true">
        <polygon points="0,0 172,0 36,260 0,260" fill="var(--navy-dark)"/>
        <polygon points="172,0 186,0 50,260 36,260" fill="var(--white)"/>
      </svg>

      <div class="person">
        <div class="person__name">MARCUS HELLER</div>
        <div class="person__title">Managing Director</div>
      </div>

      <div class="divider"></div>

      <ul class="contact">
        <li class="contact__item">
          <svg class="contact__icon" viewBox="0 0 24 24" aria-hidden="true"><path fill="#fff" d="M3 8c0-2 4-4 9-4s9 2 9 4v2h-4V8.5c-1-.6-3-1-5-1s-4 .4-5 1V10H3zM7 11h10l3 7v2H4v-2zm5 2a2.5 2.5 0 1 0 0 5 2.5 2.5 0 0 0 0-5z"/></svg>
          Panama : +507 391 4786
        </li>
        <li class="contact__item">
          <svg class="contact__icon" viewBox="0 0 24 24" aria-hidden="true"><path fill="#fff" d="M3 8c0-2 4-4 9-4s9 2 9 4v2h-4V8.5c-1-.6-3-1-5-1s-4 .4-5 1V10H3zM7 11h10l3 7v2H4v-2zm5 2a2.5 2.5 0 1 0 0 5 2.5 2.5 0 0 0 0-5z"/></svg>
          Switzerland : +41 43 917 2648
        </li>
        <li class="contact__item">
          <svg class="contact__icon" viewBox="0 0 24 24" aria-hidden="true"><rect x="3" y="6" width="18" height="13" fill="none" stroke="#fff" stroke-width="1.8"/><path d="M3 6l9 7 9-7M3 19l7-6M21 19l-7-6" fill="none" stroke="#fff" stroke-width="1.6"/></svg>
          test@borrowdale-equity-example.com
        </li>
        <li class="contact__item">
          <svg class="contact__icon" viewBox="0 0 24 24" aria-hidden="true"><circle cx="11" cy="11" r="8" fill="none" stroke="#fff" stroke-width="1.8"/><path d="M3 11h16M11 3c-3 3-3 13 0 16M11 3c3 3 3 13 0 16" fill="none" stroke="#fff" stroke-width="1.4"/><path d="M14 14l8 3-3 1-1 3z" fill="#fff"/></svg>
          www.borrowdale-equity-example.com
        </li>
      </ul>
    </div>
  </section>

  <section class="card card--back" aria-label="Business card back">
    <div class="wordmark">
      <span class="wordmark__line1">Borrowdale</span>
      <span class="wordmark__line2">Equity</span>
    </div>

    <div class="url-band">
      <svg width="948" height="64" viewBox="0 0 948 64" aria-hidden="true">
        <polygon points="0,0 104,0 72,64 0,64" fill="var(--navy-dark)"/>
        <polygon points="124,0 948,0 948,64 92,64" fill="var(--navy)"/>
      </svg>
      <div class="url-band__text">WWW.BORROWDALE-EQUITY-EXAMPLE.COM</div>
    </div>
  </section>

</main>
</body>
</html>
```